The Coral Clinic PowerPoint Design

We are looking for a new PowerPoint template design to reflect our branding and to be used for presentations at international conferences and online conferences. An example of our current template which is outdated is attached. We would like to still have a blue colour background as this represents water (but the exact background can be modified). We would like a professional, modern, and sharp feel to the templates. The template should include an Intro Slide, content slide, and closing/questions slide. The template needs to be prepared for both the standards, the 4:3 and Wide screen 16:9. Logos and branding in the attached power point can be used. Please visit our website www.thecoralclinic.example to see more about the company.

```html
<!DOCTYPE html>
<html lang="en">
<head>
<meta charset="utf-8">
<title>The Coral Clinic – Presentation Template</title>
<link rel="stylesheet" href="https://fonts.googleapis.com/css2?family=Archivo+Black&family=Arimo:wght@400;700&display=swap">
<style>
:root{
  --navy:#0b1f5c;
  --deep:#0a2a9c;
  --deep-dark:#061a6e;
  --ice:#e6f6fb;
  --ice-2:#cfeef7;
  --wave-1:#8fd6ea;
  --wave-2:#4fbcdc;
  --wave-3:#2aa6d0;
  --s1:#0b2a6b;
  --s2:#1c6fc4;
  --s3:#b9c6e6;
  --row:#b7d7ee;
  --row-alt:#d6e9f6;
  --badge:rgba(255,255,255,.28);
  --white:#ffffff;
}
*{box-sizing:border-box;margin:0;padding:0}
html,body{width:1200px;height:688px;overflow:hidden;background:#ffffff}
body{position:relative;font-family:"Arimo",Arial,sans-serif;color:var(--navy)}
.slide{position:absolute;width:390px;height:219px;overflow:hidden;
  background:linear-gradient(180deg,#f1fafd 0%,var(--ice) 45%,var(--ice-2) 100%)}
.slide.dark{background:linear-gradient(160deg,var(--deep) 0%,var(--deep-dark) 100%)}
.col-1{left:0}.col-2{left:405px}.col-3{left:810px}
.row-1{top:0}.row-2{top:234px}.row-3{top:469px}
.abs{position:absolute}
.waves{position:absolute;left:0;bottom:0;width:390px;height:62px}
.slide-title{position:absolute;left:11px;top:10px;font-family:"Archivo Black",Arial,sans-serif;font-size:12.4px;letter-spacing:.3px;color:var(--navy)}
.footer-brand{position:absolute;left:283px;top:204px;font-size:6px;font-weight:700;color:var(--white)}
.photo{position:absolute;border-radius:50%}
/* intro */
.intro-photo{position:absolute;left:0;top:0;width:200px;height:219px;
  background:radial-gradient(ellipse at 45% 40%,#6f7fe6 0%,#3446c6 35%,rgba(10,42,156,0) 75%)}
.intro-title{position:absolute;left:170px;width:220px;top:52px;text-align:center;font-family:"Archivo Black",Arial,sans-serif;font-size:12.4px;color:var(--white);letter-spacing:.3px}
.intro-sub{position:absolute;left:170px;width:220px;top:78px;text-align:center;font-size:8px;color:var(--white)}
.brand-lg{position:absolute;font-weight:700;color:var(--white)}
.partner-badge{position:absolute;left:250px;top:160px;width:57px;height:19px;background:var(--badge)}
/* vision */
.quote-mark{position:absolute;left:20px;top:76px;font-family:"Archivo Black",Arial,sans-serif;font-size:20px;color:var(--navy)}
.quote-rule{position:absolute;left:44px;top:88px;width:199px;height:1px;background:var(--navy)}
.quote-text{position:absolute;left:20px;top:100px;width:192px;font-size:11.4px;line-height:13.7px;color:var(--navy)}
.service{position:absolute;top:66px;width:70px;text-align:center}
.service .photo{position:relative;width:68px;height:68px;margin:0 auto}
.service-label{margin-top:15px;font-size:7.3px;color:var(--navy);letter-spacing:.2px}
/* text */
.body-copy{font-size:6px;line-height:8.55px;color:#1a1a2a}
.body-copy p+p{margin-top:5px}
.block-heading{font-size:5.9px;font-weight:700;color:#1a1a2a;padding-bottom:2px;border-bottom:.6px solid var(--navy);margin-bottom:6px}
/* tables */
.data-table{border-collapse:collapse;width:100%;font-size:5px;color:#1a1a2a}
.data-table th,.data-table td{height:10.9px;padding:0 3px;text-align:right;font-weight:400}
.data-table th:first-child,.data-table td:first-child{text-align:left}
.data-table td:first-child{font-weight:700}
.data-table th{font-size:5.6px}
.table-filled th{background:var(--navy);color:var(--white)}
.table-filled tbody tr:nth-child(odd){background:var(--row-alt)}
.table-filled tbody tr:nth-child(even){background:var(--row)}
.table-lined thead tr{border-top:.8px solid var(--navy);border-bottom:.5px solid var(--navy)}
.table-lined tbody tr{border-bottom:.4px solid #c7dbe8}
.chart{position:absolute;top:60px;width:173px;height:130px}
.chart text{font-family:"Arimo",Arial,sans-serif;font-size:4.3px;fill:#333}
/* closing */
.closing-photo{position:absolute;inset:0;
  background:radial-gradient(ellipse at 35% 25%,rgba(140,180,230,.55) 0%,rgba(60,110,200,0) 55%),linear-gradient(170deg,#2a5fb0 0%,#1d4c9e 50%,#123a86 100%)}
.closing-title{position:absolute;left:11px;top:21px;font-family:"Archivo Black",Arial,sans-serif;font-size:12.4px;color:var(--white);letter-spacing:.3px}
.follow{position:absolute;left:16px;top:207px;font-size:6.4px;color:var(--white);display:flex;align-items:center;gap:4px}
.follow .dot{width:10px;height:10px;border-radius:50%;border:1px solid var(--white)}
</style>
</head>
<body>

<!-- Intro -->
<section class="slide dark col-1 row-1">
  <div class="intro-photo" role="img" aria-label="Photo of a sea anemone on coral in deep blue water"></div>
  <svg class="waves" viewBox="0 0 390 62" preserveAspectRatio="none" aria-hidden="true">
    <path d="M0 10 C90 40 200 46 280 36 C330 30 365 22 390 16 V62 H0Z" fill="var(--wave-3)" opacity=".55"/>
    <path d="M0 26 C100 48 210 50 300 42 C340 38 370 34 390 30 V62 H0Z" fill="var(--wave-2)" opacity=".8"/>
  </svg>
  <h1 class="intro-title">PROJECT TITLE GOES HERE</h1>
  <p class="intro-sub">Project subtitle goes here</p>
  <div class="brand-lg" style="left:236px;top:132px;font-size:11px">The Coral Clinic</div>
  <div class="partner-badge" role="img" aria-label="Partner badge"></div>
</section>

<!-- Vision -->
<section class="slide col-2 row-1">
  <svg class="waves" viewBox="0 0 390 62" preserveAspectRatio="none" aria-hidden="true">
    <path d="M0 14 C90 40 200 46 280 38 C330 32 365 22 390 14 V62 H0Z" fill="var(--wave-1)" opacity=".7"/>
    <path d="M0 30 C100 50 210 52 300 44 C340 40 370 34 390 28 V62 H0Z" fill="var(--wave-2)" opacity=".8"/>
  </svg>
  <h2 class="slide-title">OUR VISION</h2>
  <div class="quote-mark">“</div>
  <div class="quote-rule"></div>
  <p class="quote-text">To advance the health and welfare of aquatic animals in aquariums and zoos globally</p>
  <div class="photo" style="left:239px;top:47px;width:132px;height:132px;background:radial-gradient(circle at 50% 45%,#3f8fd6 0%,#1b58b0 55%,#0d2f7a 100%)" role="img" aria-label="Photo of a colourful coral reef aquarium with tropical fish"></div>
  <div class="footer-brand">The Coral Clinic</div>
</section>

<!-- Services -->
<section class="slide col-3 row-1">
  <svg class="waves" viewBox="0 0 390 62" preserveAspectRatio="none" aria-hidden="true">
    <path d="M0 14 C90 40 200 46 280 38 C330 32 365 22 390 14 V62 H0Z" fill="var(--wave-1)" opacity=".7"/>
    <path d="M0 30 C100 50 210 52 300 44 C340 40 370 34 390 28 V62 H0Z" fill="var(--wave-2)" opacity=".8"/>
  </svg>
  <h2 class="slide-title">SLIDE TITLE GOES HERE</h2>
  <div class="service" style="left:15px"><div class="photo" style="background:radial-gradient(circle,#8fe0dc 0%,#3fb5c0 60%,#1c7f9a 100%)" role="img" aria-label="Photo of a penguin swimming underwater"></div><p class="service-label">CONSULTATION</p></div>
  <div class="service" style="left:111px"><div class="photo" style="background:radial-gradient(circle,#c99a5a 0%,#7a6a60 55%,#3d5a7a 100%)" role="img" aria-label="Photo of a seahorse"></div><p class="service-label">EDUCATION</p></div>
  <div class="service" style="left:207px"><div class="photo" style="background:radial-gradient(circle,#6fb3d8 0%,#2e7bb0 60%,#1c4f80 100%)" role="img" aria-label="Photo of a blue wrasse fish"></div><p class="service-label">CONFERENCES</p></div>
  <div class="service" style="left:303px"><div class="photo" style="background:radial-gradient(circle at 50% 40%,#f0a040 0%,#c0602a 30%,#1f3fcf 70%,#1530b0 100%)" role="img" aria-label="Photo of an orange jellyfish"></div><p class="service-label">REPRODUCTION</p></div>
  <div class="footer-brand">The Coral Clinic</div>
</section>

<!-- Text slide -->
<section class="slide col-1 row-2">
  <svg class="waves" viewBox="0 0 390 62" preserveAspectRatio="none" aria-hidden="true">
    <path d="M0 14 C90 40 200 46 280 38 C330 32 365 22 390 14 V62 H0Z" fill="var(--wave-1)" opacity=".7"/>
    <path d="M0 30 C100 50 210 52 300 44 C340 40 370 34 390 28 V62 H0Z" fill="var(--wave-2)" opacity=".8"/>
  </svg>
  <h2 class="slide-title" style="top:11px">TEXT SLIDE</h2>
  <div class="abs body-copy" style="left:11px;top:50px;width:368px">
    <p>Robot ipsum Peroxymire tautac bioarch heptaana organoity sene tetrakiscade streptoes entomorph. Demoaceous technoarian burpede medicoclast scaine offvorous pantos hippbiosis. Octomeister withcephaly dichlorograph catamost phrenoarchy ophidial autic. Psephy Sinomeister hoploitis basiant quadee ekast decas adrenoad glossana technourgy. Pneumatone aluminionik brephoderma abphyllous omphaloscribe nitrferous tomycetidae peroxyvirile. Pseudoer Euroitious orthitis cladoet erythroability zebitaxis patrplasia cynofid.. Iriworthy phonmorph homegynous stibioxor zipwise angioferous hypswise schizoergic. Fluoroopsida phlebosome pantanomy colade technometry encephalblast coploid hectpathy rhodoade comer.</p>
    <p>Glutarpede ophioaemia octferous pentaprismoclinic xanthcarpous superotic undecastomy anteite mangancy. Pseudourous arose photogynous gyncracy sexable cheirospeak philpede psychward tarsoful. Nippoibility tecngeny unworthy cytoclinic parthenile hexahedrolyte tropophilia bytropous. Eurive potamphagy matrimycetidae dermmetric lithoped oxalokins dolichanae Mcless nitrocarp. Ochly abarium levtion vesicoette decephalic lactlogic phyloon phlebootomy enteroparous. Platinosofy tautkin manganability plurily comth uranmania tetrakispter. Zymize ethomorph tocoation luteolithic ultraization Grecocratical thromboule cladoscribe. Spondylry myoac ophthalmoent phonyl erythronym ipsiart decakisgate. Psychcoel Christomorphic ideotaxy ergatoiatrics heterophorous otoisation antpter liptomy dactylsporous newlytic. Cephalophilia glutarchore cynocrat paucizoic countermorphous forfy.</p>
  </div>
  <div class="footer-brand">The Coral Clinic</div>
</section>

<!-- Text slide with title -->
<section class="slide col-2 row-2">
  <svg class="waves" viewBox="0 0 390 62" preserveAspectRatio="none" aria-hidden="true">
    <path d="M0 14 C90 40 200 46 280 38 C330 32 365 22 390 14 V62 H0Z" fill="var(--wave-1)" opacity=".7"/>
    <path d="M0 30 C100 50 210 52 300 44 C340 40 370 34 390 28 V62 H0Z" fill="var(--wave-2)" opacity=".8"/>
  </svg>
  <h2 class="slide-title" style="top:11px">TEXT SLIDE WITH TITLE</h2>
  <div class="abs body-copy" style="left:11px;top:50px;width:368px">
    <h3 class="block-heading">Text Heading goes here</h3>
    <p>Robot ipsum Peroxymire tautac bioarch heptaana organoity sene tetrakiscade streptoes entomorph. Demoaceous technoarian burpede medicoclast scaine offvorous pantos hippbiosis. Octomeister withcephaly dichlorograph catamost phrenoarchy ophidial autic. Psephy Sinomeister hoploitis basiant quadee ekast decas adrenoad glossana technourgy. Pneumatone aluminionik brephoderma abphyllous omphaloscribe nitrferous tomycetidae peroxyvirile. Pseudoer Euroitious orthitis cladoet erythroability zebitaxis patrplasia cynofid.. Iriworthy phonmorph homegynous stibioxor zipwise angioferous hypswise schizoergic. Fluoroopsida phlebosome pantanomy colade technometry encephalblast coploid hectpathy rhodoade comer.</p>
    <p>Glutarpede ophioaemia octferous pentaprismoclinic xanthcarpous superotic undecastomy anteite mangancy. Pseudourous arose photogynous gyncracy sexable cheirospeak philpede psychward tarsoful. Nippoibility tecngeny unworthy cytoclinic parthenile hexahedrolyte tropophilia bytropous. Eurive potamphagy matrimycetidae dermmetric lithoped oxalokins dolichanae Mcless nitrocarp. Ochly abarium levtion vesicoette decephalic lactlogic phyloon phlebootomy enteroparous. Platinosofy tautkin manganability plurily comth uranmania tetrakispter. Zymize ethomorph tocoation luteolithic ultraization Grecocratical thromboule cladoscribe. Spondylry myoac ophthalmoent phonyl erythronym ipsiart decakisgate. Psychcoel Christomorphic ideotaxy ergatoiatrics heterophorous otoisation antpter liptomy dactylsporous newlytic. Cephalophilia glutarchore cynocrat paucizoic countermorphous forfy.</p>
  </div>
  <div class="footer-brand">The Coral Clinic</div>
</section>

<!-- Two columns -->
<section class="slide col-3 row-2">
  <svg class="waves" viewBox="0 0 390 62" preserveAspectRatio="none" aria-hidden="true">
    <path d="M0 14 C90 40 200 46 280 38 C330 32 365 22 390 14 V62 H0Z" fill="var(--wave-1)" opacity=".7"/>
    <path d="M0 30 C100 50 210 52 300 44 C340 40 370 34 390 28 V62 H0Z" fill="var(--wave-2)" opacity=".8"/>
  </svg>
  <h2 class="slide-title" style="top:11px">TEXT SLIDE WITH TWO COLUMNS</h2>
  <div class="abs body-copy" style="left:11px;top:50px;width:173px">
    <h3 class="block-heading">Text Heading goes here</h3>
    <p>Robot ipsum Peroxymire tautac bioarch heptaana organoity sene tetrakiscade streptoes entomorph. Demoaceous technoarian burpede medicoclast scaine offvorous pantos hippbiosis. Iriworthy phonmorph homegynous stibioxor zipwise angioferous hypswise schizoergic. Fluoroopsida phlebosome pantanomy colade technometry encephalblast coploid hectpathy rhodoade comer.</p>
    <p>Glutarpede ophioaemia octferous pentaprismoclinic xanthcarpous superotic undecastomy anteite mangancy. Pseudourous arose photogynous gyncracy sexable cheirospeak philpede psychward tarsoful. Nippoibility tecngeny unworthy cytoclinic parthenile hexahedrolyte tropophilia bytropous. Eurive potamphagy matrimycetidae dermmetric lithoped oxalokins dolichanae Mcless nitrocarp.</p>
  </div>
  <div class="abs body-copy" style="left:207px;top:50px;width:173px">
    <h3 class="block-heading">Text Heading goes here</h3>
    <p>Robot ipsum Peroxymire tautac bioarch heptaana organoity sene tetrakiscade streptoes entomorph. Demoaceous technoarian burpede medicoclast scaine offvorous pantos hippbiosis. Iriworthy phonmorph homegynous stibioxor zipwise angioferous hypswise schizoergic. Fluoroopsida phlebosome pantanomy colade technometry encephalblast coploid hectpathy rhodoade comer.</p>
    <p>Glutarpede ophioaemia octferous pentaprismoclinic xanthcarpous superotic undecastomy anteite mangancy. Pseudourous arose photogynous gyncracy sexable cheirospeak philpede psychward tarsoful. Nippoibility tecngeny unworthy cytoclinic parthenile hexahedrolyte tropophilia bytropous. Eurive potamphagy matrimycetidae dermmetric lithoped oxalokins dolichanae Mcless nitrocarp.</p>
  </div>
  <div class="footer-brand">The Coral Clinic</div>
</section>

<!-- Table slide -->
<section class="slide col-1 row-3">
  <svg class="waves" viewBox="0 0 390 62" preserveAspectRatio="none" aria-hidden="true">
    <path d="M0 14 C90 40 200 46 280 38 C330 32 365 22 390 14 V62 H0Z" fill="var(--wave-1)" opacity=".7"/>
    <path d="M0 30 C100 50 210 52 300 44 C340 40 370 34 390 28 V62 H0Z" fill="var(--wave-2)" opacity=".8"/>
  </svg>
  <h2 class="slide-title" style="top:11px">TABLE SLIDE</h2>
  <div class="abs" style="left:10px;top:51px;width:174px">
    <h3 class="block-heading" style="margin-bottom:2px;padding-left:1px">Text Heading goes here</h3>
    <table class="data-table table-filled">
      <thead><tr><th>Column 1</th><th>Column 2</th><th>Column 3</th><th>Column 4</th><th>Column 5</th></tr></thead>
      <tbody>
        <tr><td>Row 1</td><td>3892</td><td>643</td><td>366</td><td>44%</td></tr>
        <tr><td>Row 2</td><td>324</td><td>5232</td><td>86</td><td>6%</td></tr>
        <tr><td>Row 3</td><td>232</td><td>8575</td><td>35</td><td>7%</td></tr>
        <tr><td>Row 4</td><td>4</td><td>9868</td><td>625</td><td>33%</td></tr>
        <tr><td>Row 5</td><td>333</td><td>4553</td><td>679</td><td>85%</td></tr>
        <tr><td>Row 6</td><td>22</td><td>79</td><td>45</td><td>44%</td></tr>
        <tr><td>Row 7</td><td>5465</td><td>57</td><td>898</td><td>78%</td></tr>
        <tr><td>Row 8</td><td>578</td><td>435</td><td>43</td><td>98%</td></tr>
        <tr><td>Row 9</td><td>-</td><td>68</td><td>699</td><td>45%</td></tr>
        <tr><td>Row 10</td><td>876</td><td>599</td><td>55</td><td>68%</td></tr>
      </tbody>
    </table>
  </div>
  <div class="abs" style="left:207px;top:51px;width:173px">
    <h3 class="block-heading" style="margin-bottom:2px;padding-left:1px">Text Heading goes here</h3>
    <table class="data-table table-lined">
      <thead><tr><th>Column 1</th><th>Column 2</th><th>Column 3</th><th>Column 4</th><th>Column 5</th></tr></thead>
      <tbody>
        <tr><td>Row 1</td><td>3892</td><td>643</td><td>366</td><td>44%</td></tr>
        <tr><td>Row 2</td><td>324</td><td>5232</td><td>86</td><td>6%</td></tr>
        <tr><td>Row 3</td><td>232</td><td>8575</td><td>35</td><td>7%</td></tr>
        <tr><td>Row 4</td><td>4</td><td>9868</td><td>625</td><td>33%</td></tr>
        <tr><td>Row 5</td><td>333</td><td>4553</td><td>679</td><td>85%</td></tr>
        <tr><td>Row 6</td><td>22</td><td>79</td><td>45</td><td>44%</td></tr>
        <tr><td>Row 7</td><td>5465</td><td>57</td><td>898</td><td>78%</td></tr>
        <tr><td>Row 8</td><td>578</td><td>435</td><td>43</td><td>98%</td></tr>
        <tr><td>Row 9</td><td>-</td><td>68</td><td>699</td><td>45%</td></tr>
        <tr><td>Row 10</td><td>876</td><td>599</td><td>55</td><td>68%</td></tr>
      </tbody>
    </table>
  </div>
  <div class="footer-brand">The Coral Clinic</div>
</section>

<!-- Chart slide -->
<section class="slide col-2 row-3">
  <svg class="waves" viewBox="0 0 390 62" preserveAspectRatio="none" aria-hidden="true">
    <path d="M0 14 C90 40 200 46 280 38 C330 32 365 22 390 14 V62 H0Z" fill="var(--wave-1)" opacity=".7"/>
    <path d="M0 30 C100 50 210 52 300 44 C340 40 370 34 390 28 V62 H0Z" fill="var(--wave-2)" opacity=".8"/>
  </svg>
  <h2 class="slide-title" style="top:11px">CHART SLIDE</h2>
  <h3 class="abs block-heading" style="left:11px;top:51px;width:173px">Text Heading goes here</h3>
  <h3 class="abs block-heading" style="left:207px;top:51px;width:173px">Text Heading goes here</h3>
  <svg class="chart" style="left:11px" viewBox="0 0 173 130" aria-label="Bar chart of three series across four categories">
    <g text-anchor="start"><text x="1" y="7">6</text><text x="1" y="23">5</text><text x="1" y="39">4</text><text x="1" y="55">3</text><text x="1" y="71">2</text><text x="1" y="87">1</text><text x="1" y="103">0</text></g>
    <g fill="var(--s1)"><rect x="16" y="31.2" width="6" height="68.8"/><rect x="55" y="60" width="6" height="40"/><rect x="94" y="44" width="6" height="56"/><rect x="133" y="28" width="6" height="72"/></g>
    <g fill="var(--s2)"><rect x="24" y="61.6" width="6" height="38.4"/><rect x="63" y="29.6" width="6" height="70.4"/><rect x="102" y="71.2" width="6" height="28.8"/><rect x="141" y="55.2" width="6" height="44.8"/></g>
    <g fill="var(--s3)"><rect x="32" y="68" width="6" height="32"/><rect x="71" y="68" width="6" height="32"/><rect x="110" y="52" width="6" height="48"/><rect x="149" y="20" width="6" height="80"/></g>
    <g text-anchor="middle"><text x="27" y="108">Category 1</text><text x="66" y="108">Category 2</text><text x="105" y="108">Category 3</text><text x="144" y="108">Category 4</text></g>
    <rect x="51" y="114.5" width="3" height="3" fill="var(--s1)"/><text x="55.5" y="117.5">Series 1</text>
    <rect x="76" y="114.5" width="3" height="3" fill="var(--s2)"/><text x="80.5" y="117.5">Series 2</text>
    <rect x="101" y="114.5" width="3" height="3" fill="var(--s3)"/><text x="105.5" y="117.5">Series 3</text>
  </svg>
  <svg class="chart" style="left:207px" viewBox="0 0 173 130" aria-label="Line chart of three series across four categories">
    <g text-anchor="start"><text x="1" y="7">6</text><text x="1" y="23">5</text><text x="1" y="39">4</text><text x="1" y="55">3</text><text x="1" y="71">2</text><text x="1" y="87">1</text><text x="1" y="103">0</text></g>
    <g fill="none" stroke-width="1">
      <polyline stroke="var(--s3)" points="33.5,68 72.5,68 111.5,52 150.5,20"/>
      <polyline stroke="var(--s2)" points="33.5,61.6 72.5,29.6 111.5,71.2 150.5,55.2"/>
      <polyline stroke="var(--s1)" points="33.5,31.2 72.5,60 111.5,44 150.5,28"/>
    </g>
    <g text-anchor="middle"><text x="33.5" y="108">Category 1</text><text x="72.5" y="108">Category 2</text><text x="111.5" y="108">Category 3</text><text x="150.5" y="108">Category 4</text></g>
    <line x1="44" y1="116" x2="51" y2="116" stroke="var(--s1)"/><text x="52.5" y="117.5">Series 1</text>
    <line x1="72" y1="116" x2="79" y2="116" stroke="var(--s2)"/><text x="80.5" y="117.5">Series 2</text>
    <line x1="100" y1="116" x2="107" y2="116" stroke="var(--s3)"/><text x="108.5" y="117.5">Series 3</text>
  </svg>
  <div class="footer-brand">The Coral Clinic</div>
</section>

<!-- Closing -->
<section class="slide dark col-3 row-3">
  <div class="closing-photo" role="img" aria-label="Photo of a manta ray swimming with a school of fish in a large aquarium"></div>
  <svg class="waves" viewBox="0 0 390 62" preserveAspectRatio="none" aria-hidden="true">
    <path d="M0 24 C100 46 210 50 300 42 C340 38 370 32 390 28 V62 H0Z" fill="var(--wave-3)" opacity=".45"/>
  </svg>
  <h2 class="closing-title">THANK YOU</h2>
  <div class="brand-lg" style="left:252px;top:26px;font-size:12px">The Coral Clinic</div>
  <div class="follow">Follow The Coral Clinic on <span class="dot"></span></div>
</section>

</body>
</html>
```